Pizza Snack Pack Design

The design of sleeve for “Crumb Carnival” packs, this is a tray of cheese & pizza flavored snack bread.
Sleeve covers the tray and offers two circular windows on the sleeve to show the cheese and snack bread.
With this project we are looking to convey to consumer that he/she is having pizza snack.
This is for the convenience or “food to go” section of the stores.

We have the information that will be printed on the base of the pack including ingredients, pack weight, bar code etc. it is important for the designer to focus on the top and side panels.
There is no limit to the number of colors can be used as we will be printing full color.

Target Market(s)

Any pizza loving person, 12 years and above, office workers, travelers, university students
Convenience stores, shops at airports, train stations, petrol stations.

Industry/Entity Type

Printing

Font styles to use
Serif
Sans Serif
Decorative
Script

Requirements
Must have
• Design for the sleeve on tray containing dip & snack bread that offers two windows to show the contents.
• The sleeve dimension The width is 158mm and Height is 181mm that includes 20mm overlap.
• The tray dimension: L: 160mm W: 75mm H: 27mm.
• Note: The design is more important than getting the dimension correct. All emphasis should be on the top and side panels. We will add the content details in-house.
Nice to have
• Strong emphasis on pizza flavor of the snack pack.
• Re-design of the pack name i.e. the Crumb Carnival writing to suit the new design.
Should not have
• Avoid clatter of shapes and writing and color clash.
• The design must tell the content within 10 second of consumer looking at it.

```html
<!DOCTYPE html>
<html lang="en">
<head>
<meta charset="utf-8">
<title>Crumb Carnival – Sleeve Design</title>
<link rel="stylesheet" href="https://fonts.googleapis.com/css2?family=Rokkitt:wght@400;700&family=Dancing+Script:wght@500&display=swap">
<style>
  :root {
    --page-bg: #ffffff;
    --navy-deep: #0a2f86;
    --navy-mid: #0d4fb8;
    --blue-bright: #1c7fe0;
    --stripe-cyan: #00a3e6;
    --gold: #c99a4e;
    --gold-light: #f1d29a;
    --window-black: #000000;
    --ink-navy: #0b2a6b;
    --text-white: #ffffff;
  }
  html, body {
    margin: 0;
    width: 1200px;
    height: 1000px;
    overflow: hidden;
    background: var(--page-bg);
  }
  .canvas {
    position: relative;
    width: 1200px;
    height: 1000px;
  }
  .sleeve {
    position: absolute;
    left: 150px;
    top: 34px;
    width: 928px;
    height: 571px;
  }
  .sleeve-art {
    position: absolute;
    inset: 0;
  }
  .brand-name {
    position: absolute;
    margin: 0;
    font-family: "Rokkitt", serif;
    font-weight: 700;
    color: var(--text-white);
    line-height: 0.92;
    text-align: center;
  }
  .top-panel .brand-name {
    left: 320px;
    top: 100px;
    width: 320px;
    font-size: 62px;
  }
  .side-panel .brand-name {
    left: 105px;
    top: 450px;
    width: 240px;
    font-size: 46px;
  }
  .product-name {
    position: absolute;
    margin: 0;
    font-family: "Rokkitt", serif;
    font-weight: 400;
    color: var(--ink-navy);
    border-bottom: 2px solid var(--ink-navy);
    white-space: nowrap;
    text-align: center;
  }
  .top-panel .product-name {
    left: 304px;
    top: 296px;
    width: 332px;
    font-size: 29px;
    line-height: 30px;
  }
  .side-panel .product-name {
    left: 384px;
    top: 460px;
    width: 436px;
    font-size: 40px;
    line-height: 40px;
  }
  .tagline {
    position: absolute;
    margin: 0;
    font-family: "Dancing Script", cursive;
    font-weight: 500;
    color: var(--text-white);
    white-space: nowrap;
    text-align: center;
  }
  .top-panel .tagline {
    left: 290px;
    top: 334px;
    width: 360px;
    font-size: 20px;
  }
  .side-panel .tagline {
    left: 360px;
    top: 505px;
    width: 480px;
    font-size: 28px;
  }
</style>
</head>
<body>
<main class="canvas">
  <section class="sleeve" aria-label="Crumb Carnival sleeve">
    <svg class="sleeve-art" width="928" height="571" viewBox="0 0 928 571" aria-hidden="true">
      <defs>
        <radialGradient id="panel-glow" cx="0.5" cy="0.55" r="0.7">
          <stop offset="0" stop-color="#1f8ae8"/>
          <stop offset="0.55" stop-color="#0d56c0"/>
          <stop offset="1" stop-color="#0a2f86"/>
        </radialGradient>
        <linearGradient id="gold-line" x1="0" x2="1" y1="0" y2="0">
          <stop offset="0" stop-color="#a8742e"/>
          <stop offset="0.5" stop-color="#f1d29a"/>
          <stop offset="1" stop-color="#a8742e"/>
        </linearGradient>
        <path id="window-shape" d="M88.9,-23.8 Q122,0 88.9,23.8 Q105.7,61 65.1,65.1 Q61,105.7 23.8,88.9 Q0,122 -23.8,88.9 Q-61,105.7 -65.1,65.1 Q-105.7,61 -88.9,23.8 Q-122,0 -88.9,-23.8 Q-105.7,-61 -65.1,-65.1 Q-61,-105.7 -23.8,-88.9 Q0,-122 23.8,-88.9 Q61,-105.7 65.1,-65.1 Q105.7,-61 88.9,-23.8Z"/>
      </defs>

      <!-- top panel -->
      <rect class="top-stripe" x="0" y="0" width="928" height="12" fill="#00a3e6"/>
      <rect class="top-panel-bg" x="0" y="12" width="928" height="397" fill="url(#panel-glow)"/>
      <path class="swoosh-band" d="M0,150 Q420,20 928,116 L928,226 Q470,170 0,408 Z" fill="#1670d8" opacity="0.75"/>
      <path class="gold-arc upper" d="M0,150 Q420,20 928,116" fill="none" stroke="url(#gold-line)" stroke-width="4"/>
      <path class="gold-arc lower" d="M0,408 Q470,170 928,226" fill="none" stroke="url(#gold-line)" stroke-width="4"/>

      <!-- windows -->
      <g class="window left" transform="translate(208,213)">
        <use href="#window-shape" fill="#000" stroke="#d7aa62" stroke-width="6"/>
      </g>
      <g class="window right" transform="translate(726,213)">
        <use href="#window-shape" fill="#000" stroke="#d7aa62" stroke-width="6"/>
      </g>

      <!-- side panel -->
      <rect class="divider-stripe" x="0" y="409" width="928" height="17" fill="#00a3e6"/>
      <rect class="side-panel-bg" x="0" y="426" width="928" height="145" fill="url(#panel-glow)"/>
    </svg>

    <div class="top-panel">
      <h1 class="brand-name">Crumb<br>Carnival</h1>
      <p class="product-name">Cheese &amp; Pizza Bread</p>
      <p class="tagline">A tasty snack for any time of the day!</p>
    </div>

    <div class="side-panel">
      <p class="brand-name">Crumb<br>Carnival</p>
      <p class="product-name">Cheese &amp; Pizza Bread</p>
      <p class="tagline">A tasty snack for any time of the day!</p>
    </div>
  </section>
</main>
</body>
</html>
```